Tabloid Magazine Flyer Class Action Lawsuit

Create a bold, 2-page 8.5" x 11" flyer with the look and feel of a tabloid exposé — loud, sensational, and impossible to ignore. Use bold fonts, dramatic headlines, and high-contrast colors (red, black, white, deep blue). Fill every inch of space — no white space, no subtlety. Use the provided images prominently. Page 1 should grab attention with a shocking headline, impactful image, and strong call to action. Page 2 should stack bold subheadings and explosive bullet points. Emphasize urgency, outrage, and grassroots power. This flyer is meant to rally a community.
Updates

Need to extend because we haven't received a design that meets our needs

Target Market(s)

All instructions and content are in the attached word doc

Industry/Entity Type

Requirements
Must have
• All instructions and content are in the attached word doc
Nice to have
Should not have

```html
<!DOCTYPE html>
<html lang="en">
<head>
<meta charset="utf-8">
<title>Harborview Park Tabloid Flyer</title>
<link href="https://fonts.googleapis.com/css2?family=Anton&family=Poppins:wght@600;700;800&display=swap" rel="stylesheet">
<style>
:root{
  --navy:#26356a;
  --blue:#21438f;
  --red:#d32027;
  --yellow:#fff200;
  --black:#000;
  --white:#fff;
  --stage:#b4b4b4;
}
*{margin:0;padding:0;box-sizing:border-box}
html,body{width:1200px;height:1117px;overflow:hidden;background:var(--stage)}
.canvas{position:relative;width:1200px;height:1117px}
.page{position:absolute;top:239px;width:539px;height:701px;overflow:hidden}
.page--front{left:51px;background:var(--blue)}
.page--back{left:616px;background:var(--white)}
.abs{position:absolute}
.condensed{font-family:'Anton',sans-serif;text-transform:uppercase;letter-spacing:.2px}
.sans{font-family:'Poppins',sans-serif}

/* FRONT */
.hero{left:0;top:0;width:539px;height:261px;background:linear-gradient(90deg,var(--navy) 0%,var(--navy) 50%,#3c4e86 62%,#8fa6c7 100%)}
.hero-photo{left:305px;top:0;width:234px;height:261px;background:linear-gradient(180deg,#a9c6e3 0%,#c98b8c 45%,#7a4a52 100%);opacity:.85}
.headline{left:26px;top:18px;color:var(--white);font-size:30px;line-height:31px;text-shadow:2px 2px 3px rgba(0,0,0,.6)}
.headline-call{left:26px;top:181px;color:var(--yellow);font-size:32px;line-height:33px;text-shadow:2px 2px 3px rgba(0,0,0,.6)}
.public-band{left:0;top:261px;width:539px;height:71px;background:var(--red);color:var(--white);font-size:15.5px;font-weight:700;line-height:18px;text-align:center;padding:10px 90px 0 0}
.stop-sign{left:411px;top:212px;width:118px;height:118px}
.meeting{left:0;top:342px;width:273px;text-align:center;color:var(--white)}
.meeting-join{font-size:10px;font-weight:700;line-height:12px}
.meeting-name{font-size:19px;font-weight:800;line-height:19px;margin-top:3px}
.meeting-date{left:32px;top:398px;width:222px;height:22px;background:var(--yellow);color:var(--black);font-size:13px;font-weight:800;line-height:22px;text-align:center}
.meeting-place{left:32px;top:427px;width:240px;color:var(--white);font-size:9.5px;font-weight:700;line-height:11px}
.meeting-place b{color:var(--yellow)}
.cta-stack{text-align:center}
.cta-box{display:inline-block;line-height:1;padding:2px 5px}
.cta-front{left:268px;top:342px;width:260px}
.cta-front .l1{background:var(--red);color:var(--yellow);font-size:25px}
.cta-front .l2{background:var(--red);color:var(--white);font-size:20px}
.cta-front .l3{background:var(--red);color:var(--white);font-size:46px;padding:3px 8px}
.venue-photo{left:0;top:458px;width:273px;height:183px;background:linear-gradient(180deg,#b9cbe0 0%,#8fa0b6 45%,#2f6fa6 75%,#2b3a52 100%)}
.partner-badge{left:0;top:580px;width:133px;height:61px;background:var(--white)}
.lawsuit{left:283px;top:496px;width:256px;height:145px;background:var(--yellow);text-align:center;padding-top:10px}
.lawsuit-title{font-size:21px;line-height:22px;color:var(--black)}
.lawsuit-body{font-size:10.6px;font-weight:800;line-height:13px;color:var(--black);margin-top:4px;text-transform:uppercase;padding:0 6px}
.footer{left:0;width:539px;background:var(--black);color:var(--white);font-weight:700;text-align:center}
.page--front .footer{top:641px;height:60px;font-size:33px;line-height:60px}

/* BACK */
.exposed-intro{left:8px;top:8px;width:234px;height:159px;background:var(--navy);color:var(--white);font-size:10.6px;font-weight:700;line-height:13px;text-align:center;padding:17px 8px 0}
.exposed-intro b{color:var(--yellow)}
.tower-photo{left:242px;top:8px;width:289px;height:159px;background:linear-gradient(180deg,#233a78 0%,#c9562f 45%,#f3a13a 60%,#3a3540 100%)}
.know-band{left:8px;top:167px;width:523px;height:42px;background:var(--yellow);color:var(--black);font-size:21px;font-weight:800;line-height:42px;text-align:center;letter-spacing:-.3px}
.blue-backdrop{left:8px;top:209px;width:523px;height:201px;background:var(--blue)}
.column{background:var(--red);color:var(--white);padding:9px 8px 0 14px}
.column--left{left:23px;top:209px;width:257px;height:419px}
.column--right{left:280px;top:209px;width:234px;height:271px;padding-left:0}
.item{margin-bottom:9px}
.item h3{color:var(--yellow);font-size:10px;font-weight:700;line-height:11px;text-transform:uppercase}
.item p{font-size:8.6px;font-weight:600;line-height:10.3px}
.cta-back{left:291px;top:494px;width:223px}
.cta-back .l1{background:var(--blue);color:var(--yellow);font-size:21px}
.cta-back .l2{background:var(--blue);color:var(--white);font-size:18px}
.cta-back .l3{background:var(--blue);color:var(--white);font-size:40px;padding:3px 8px}
.page--back .footer{left:8px;top:634px;width:523px;height:59px;font-size:32px;line-height:59px}
</style>
</head>
<body>
<div class="canvas">

  <section class="page page--front">
    <div class="abs hero"></div>
    <div class="abs hero-photo" role="img" aria-label="Crowd at a packed beach rave with a performer raising her arms"></div>
    <h1 class="abs headline condensed">Harborview Park<br>Exposed Disabled<br>Child Traumatized<br>Public Land<br>Abused For Profit</h1>
    <h2 class="abs headline-call condensed">Help Our Beach<br>Community Fight Back</h2>

    <p class="abs public-band sans">HARBORVIEW PARK IS NOT PRIVATE.<br>IT IS PUBLIC PROPERTY OWNED BY THE CITY,<br>PAID FOR BY YOU.</p>

    <svg class="abs stop-sign" viewBox="0 0 118 118" aria-label="Stop sign: no public access">
      <polygon points="35,2 83,2 116,35 116,83 83,116 35,116 2,83 2,35" fill="#fff"/>
      <polygon points="37,7 81,7 111,37 111,81 81,111 37,111 7,81 7,37" fill="#d32027"/>
      <text x="59" y="46" text-anchor="middle" font-family="Anton, sans-serif" font-size="30" fill="#fff">STOP</text>
      <rect x="14" y="53" width="90" height="48" fill="#fff"/>
      <text x="59" y="75" text-anchor="middle" font-family="Anton, sans-serif" font-size="19" fill="#d32027">NO PUBLIC</text>
      <text x="59" y="97" text-anchor="middle" font-family="Anton, sans-serif" font-size="19" fill="#d32027">ACCESS</text>
    </svg>

    <div class="abs meeting sans">
      <p class="meeting-join">JOIN US &amp; SHOW YOUR SUPPORT @</p>
      <p class="meeting-name">SEACREST BEACH TOWN<br>COUNCIL MEETING</p>
    </div>
    <p class="abs meeting-date sans">DATE: MAY 14, 2025 – 6:00 PM</p>
    <p class="abs meeting-place sans"><b>PLACE:</b> HARBORVIEW PARK COMMUNITY ROOM<br>&nbsp;&nbsp;&nbsp;&nbsp;&nbsp;&nbsp;&nbsp;&nbsp;&nbsp;&nbsp;&nbsp;(ABOVE THE ARCADE)</p>

    <div class="abs cta-stack cta-front condensed">
      <span class="cta-box l1">Help Our Community<br>Save Harborview Park</span><br>
      <span class="cta-box l2">Harborview Park Was Built<br>For Families —</span><br>
      <span class="cta-box l3">NoTraves</span>
    </div>

    <div class="abs venue-photo" role="img" aria-label="Park entrance with a row of portable toilets in front of a roller coaster"></div>
    <div class="abs partner-badge" aria-hidden="true"></div>

    <div class="abs lawsuit">
      <p class="lawsuit-title condensed">Class Action<br>Lawsuit Forming Now!</p>
      <p class="lawsuit-body sans">If you’ve been impacted by noise, denied public access, or harmed by these violations, you may be eligible for compensation. We’re gathering stories and preparing legal action.</p>
    </div>

    <p class="abs footer sans">www.FixHarborviewPark.com</p>
  </section>

  <section class="page page--back">
    <p class="abs exposed-intro sans"><b>XPOSED: Marco Valenti,</b> CEO of Crescent Holdings Pool IX LLC the leaseholder of Harborview Park, has drawn community outrage for profiting off public land while operating Harborview Park in ways many say violate its lease and damage our beach, our peace, and our environment — all from his luxury estate in Oak Hollow.</p>
    <div class="abs tower-photo" role="img" aria-label="Lifeguard tower on the beach at sunset"></div>
    <h2 class="abs know-band sans">WHAT THEY DON’T WANT YOU TO KNOW:</h2>
    <div class="abs blue-backdrop"></div>

    <div class="abs column column--left sans">
      <div class="item"><h3>Illegal Raves – No Permits.</h3><p>Explosive concerts over 100 decibels, blasting Seacrest Beach with bass — multiple times per week. According to Public Records these events had <b>NO PERMITS &amp; NO CITY APPROVAL.</b></p></div>
      <div class="item"><h3>The Beach House isn’t<br>theirs – it’s yours.</h3><p>Harborview Park is shutting down public space for 9 private Beach House raves through July. But July 5 is different — “Liberty Blast” is a full-park, alcohol-fueled rave that shuts out the public from taxpayer-owned land. These takeovers appear to violate their lease and Prop G, which protects YOUR beach for ALL — not just paying partiers.</p></div>
      <div class="item"><h3>Disabled Child Traumatized<br>by Rave Noise</h3><p>A child with cerebral palsy and auditory sensitivity came to use the City’s Beach Accessibility Program but was overwhelmed by deafening Rave noise and fled in distress. The illegal sound levels deny All individuals with similar disabilities access to public accommodations. This is a direct violation of the Americans with Disabilities Act.</p></div>
      <div class="item"><h3>Exposed: Is Harborview Running an<br>Unethical Self-Dealing Scheme?</h3><p>Harborview Park’s General Manager, Glen Porter, is also CEO of GP Guard Services — the very company hired by Harborview for “security” services. And who’s listed as corporate secretary? Lena Valenti, close relative of the leaseholder Marco Valenti. Is this Self-Dealing?</p></div>
    </div>

    <div class="abs column column--right sans">
      <div class="item"><h3>Documented Runoff and Suspected<br>Environmental Disaster</h3><p>Improperly Stored Chemicals, oils, and waste water spilling into storm drains. Parking lots are trashed, flooded, and neglected. Stormwater compliance appears to be ignored.</p></div>
      <div class="item"><h3>Exposed: Harborview Park’s Illegal<br>Signs Mislead the Public.</h3><p>They’re tricking the public into believing city-owned land is private, violating their lease which requires signage clearly stating the property is city-owned and open to all.</p></div>
      <div class="item"><h3>Harborview Park: Accident Waiting<br>to Happen?</h3><p>From the Big Swoop to the rides and walkways, safety appears ignored. The lease requires independent engineer inspections — yet no reports can be found. With what looks like hundreds of code violations, the entire park may be one broken bolt from disaster. Who’s protecting the public?</p></div>
    </div>

    <div class="abs cta-stack cta-back condensed">
      <span class="cta-box l1">Help Our Community<br>Save Harborview Park</span><br>
      <span class="cta-box l2">Harborview Park Was Built<br>For Families —</span><br>
      <span class="cta-box l3">NoTraves</span>
    </div>

    <p class="abs footer sans">www.FixHarborviewPark.com</p>
  </section>

</div>
</body>
</html>
```